Packaging design for children’s shampoo bar

A design that could be used on solid shampoo and soap wraps then amended for jar labels. The packaging needs to be bright and child-friendly. We have a logo and a pattern, but please feel free to change them. I think it needs to be brighter.

I would like each product to have an accent colour and for the shampoo I am thinking of blue/teal. This will be complemented by the body wash bar (pink) and toothpaste (orange).

The shampoo bar wrap needs to contain the following information:

Pippin & Pals logo
Shampoo Bar
100% natural
Vegan & Palm Oil-Free
Weight 85 g
Made in the U.K.

Ingredients: sodium hydroxide, prunus amygdalus dulcis oil, olea europaea oil, cocos nucifera oil, ricinus communis seed oil, simmondsia chinensia seed oil.

Contact details: Pippin & Pals, Marlow Tessing House, London N7 4QB. Website: www.Pippin and pals.co.U.K.

Brand board is here: https://www.filecrate.example/s/k8rw2mzatqvexbd/Photo%2003-07-2020%2C%2021%2040%2034.jpg?dl=0

Inspiration is here: https://kitebirdstudio.example/collections/beauty-grooming/products/dog-shampoo-100-natural-vegan

These are the wraps we shall be using: https://www.nearbypressworks.example/soap-wrap

Thank you so much for your interest in this project!

Target Market(s)

Children 5-12 years.

Requirements
Must have
• Clean design. Lots of white with bright colours.

```html
<!DOCTYPE html>
<html lang="en">
<head>
<meta charset="utf-8">
<title>Pippin &amp; Pals – Shampoo Bar Wrap</title>
<link href="https://fonts.googleapis.com/css2?family=Montserrat:wght@400;500;600&display=swap" rel="stylesheet">
<style>
  :root {
    --backdrop: #e2e44c;
    --teal-deep: #0a6e99;
    --teal-soft: #a9d3df;
    --lavender: #6f8fcc;
    --white: #ffffff;
    --green: #17a24a;
    --ink: #161616;
    --fold: rgba(255,255,255,0.7);
    --pink: #ef86b2;
    --salmon: #f27f6c;
    --sun: #f9d23a;
    --cream: #f6e39a;
    --orange: #ef8a3a;
    --leaf: #86c24a;
    --sky: #84c8e6;
    --grey: #8d9bb2;
    --blue: #3c7fd0;
  }
  * { box-sizing: border-box; margin: 0; padding: 0; }
  html, body { width: 1200px; height: 852px; overflow: hidden; }
  body {
    background: var(--backdrop);
    font-family: "Montserrat", sans-serif;
    position: relative;
  }
  .wrap-sheet {
    position: absolute;
    left: 244px; top: 26px;
    width: 712px; height: 800px;
    background: linear-gradient(90deg,
      var(--teal-deep) 0%, var(--teal-soft) 24%, var(--white) 34%,
      var(--white) 62%, #dbe2f2 74%, var(--lavender) 100%);
    overflow: hidden;
  }
  .fold { position: absolute; background: var(--fold); }
  .fold.v { top: 0; bottom: 0; width: 1px; }
  .fold.h { left: 0; right: 0; height: 1px; }

  .critter, .sprig {
    position: absolute;
    left: var(--x); top: var(--y);
    transform: translate(-50%, -50%);
  }
  .critter {
    width: var(--w, 46px); height: var(--h, 46px);
    border-radius: 50%;
    background: radial-gradient(circle at 38% 32%,
      color-mix(in srgb, var(--c) 45%, white) 0%, var(--c) 70%);
    box-shadow: 0 0 0 2px rgba(255,255,255,0.85);
  }
  .sprig {
    width: var(--w, 30px); height: var(--w, 30px);
    border-radius: 50% 50% 50% 50% / 35% 35% 65% 65%;
    background: linear-gradient(180deg,
      color-mix(in srgb, var(--c) 55%, white), var(--c));
    opacity: 0.9;
  }

  .front-panel {
    position: absolute;
    left: 177px; width: 356px; top: 0; bottom: 0;
    text-align: center;
    color: var(--ink);
  }
  .claims {
    position: absolute; left: 0; right: 0; top: 143px;
    color: var(--green); font-weight: 500; font-size: 17px; line-height: 1;
  }
  .claims .rule {
    display: block; width: 174px; height: 2px;
    background: var(--green); margin: 4px auto 5px;
    border-radius: 2px;
  }
  .brand-name {
    position: absolute; left: 0; right: 0; top: 222px;
    font-weight: 600; font-size: 42px; color: var(--orange);
    line-height: 1;
  }
  .product-name {
    position: absolute; left: 0; right: 0; top: 320px;
    font-weight: 500; font-size: 16px; letter-spacing: 0.3px;
  }
  .ingredients {
    position: absolute; left: 42px; right: 42px; top: 557px;
    font-size: 9.4px; line-height: 12px; font-weight: 500;
  }
  .maker {
    position: absolute; left: 0; right: 0; top: 604px;
    font-size: 9.4px; line-height: 12px; font-weight: 500; font-style: normal;
  }
  .weight {
    position: absolute; left: 48px; top: 650px;
    font-size: 16px; font-weight: 500;
  }
  .origin {
    position: absolute; left: 229px; top: 655px;
    font-size: 9.6px; font-weight: 500;
  }
</style>
</head>
<body>
  <main class="wrap-sheet">
    <div class="fold v" style="left:63px"></div>
    <div class="fold v" style="left:178px"></div>
    <div class="fold v" style="left:649px"></div>
    <div class="fold h" style="top:113px"></div>
    <div class="fold h" style="top:370px"></div>
    <div class="fold h" style="top:483px"></div>
    <div class="fold h" style="top:740px"></div>

    <div class="sprig" role="img" aria-label="Blue flower sprig" style="--x:51px;--y:22px;--w:22px;--c:var(--blue)"></div>
    <div class="sprig" role="img" aria-label="Pink leaf sprig" style="--x:54px;--y:97px;--c:var(--pink)"></div>
    <div class="sprig" role="img" aria-label="Green grass sprig" style="--x:216px;--y:40px;--c:var(--leaf)"></div>
    <div class="sprig" role="img" aria-label="Yellow leaf sprig" style="--x:421px;--y:19px;--w:24px;--c:var(--sun)"></div>
    <div class="sprig" role="img" aria-label="Pink leaf sprig" style="--x:467px;--y:70px;--c:var(--pink)"></div>
    <div class="sprig" role="img" aria-label="Yellow leaf sprig" style="--x:654px;--y:58px;--c:var(--sun)"></div>
    <div class="sprig" role="img" aria-label="Pink flower sprig" style="--x:654px;--y:130px;--w:26px;--c:var(--pink)"></div>
    <div class="sprig" role="img" aria-label="Green grass sprig" style="--x:126px;--y:214px;--c:var(--leaf)"></div>
    <div class="sprig" role="img" aria-label="Yellow leaf sprig" style="--x:54px;--y:283px;--c:var(--sun)"></div>
    <div class="sprig" role="img" aria-label="Sky blue grass sprig" style="--x:534px;--y:223px;--c:var(--sky)"></div>
    <div class="sprig" role="img" aria-label="Pink leaf sprig" style="--x:654px;--y:265px;--c:var(--pink)"></div>
    <div class="sprig" role="img" aria-label="Yellow leaf sprig" style="--x:417px;--y:364px;--w:24px;--c:var(--sun)"></div>
    <div class="sprig" role="img" aria-label="Green grass sprig" style="--x:261px;--y:412px;--c:var(--leaf)"></div>
    <div class="sprig" role="img" aria-label="Blue flower sprig" style="--x:459px;--y:424px;--w:22px;--c:var(--blue)"></div>
    <div class="sprig" role="img" aria-label="Green grass sprig" style="--x:684px;--y:391px;--w:24px;--c:var(--leaf)"></div>
    <div class="sprig" role="img" aria-label="Pink leaf sprig" style="--x:141px;--y:451px;--w:28px;--c:var(--pink)"></div>
    <div class="sprig" role="img" aria-label="Yellow leaf sprig" style="--x:459px;--y:520px;--c:var(--sun)"></div>
    <div class="sprig" role="img" aria-label="Pink flower sprig" style="--x:183px;--y:598px;--w:24px;--c:var(--pink)"></div>
    <div class="sprig" role="img" aria-label="Yellow leaf sprig" style="--x:591px;--y:574px;--c:var(--sun)"></div>
    <div class="sprig" role="img" aria-label="Yellow leaf sprig" style="--x:129px;--y:694px;--c:var(--sun)"></div>
    <div class="sprig" role="img" aria-label="Sky blue grass sprig" style="--x:306px;--y:670px;--c:var(--sky)"></div>
    <div class="sprig" role="img" aria-label="Blue flower sprig" style="--x:429px;--y:700px;--w:22px;--c:var(--blue)"></div>
    <div class="sprig" role="img" aria-label="Yellow leaf sprig" style="--x:669px;--y:718px;--c:var(--sun)"></div>
    <div class="sprig" role="img" aria-label="Sky blue grass sprig" style="--x:222px;--y:775px;--c:var(--sky)"></div>
    <div class="sprig" role="img" aria-label="Pink leaf sprig" style="--x:501px;--y:775px;--c:var(--pink)"></div>

    <div class="critter" role="img" aria-label="Cartoon panda" style="--x:153px;--y:70px;--w:40px;--h:50px;--c:var(--grey)"></div>
    <div class="critter" role="img" aria-label="Cartoon pig" style="--x:393px;--y:58px;--w:66px;--h:44px;--c:var(--salmon)"></div>
    <div class="critter" role="img" aria-label="Pastel rainbow" style="--x:288px;--y:90px;--w:56px;--h:44px;--c:var(--pink)"></div>
    <div class="critter" role="img" aria-label="Cartoon cat" style="--x:567px;--y:79px;--w:44px;--h:56px;--c:var(--cream)"></div>
    <div class="critter" role="img" aria-label="Cartoon rabbit" style="--x:44px;--y:196px;--w:38px;--h:70px;--c:var(--cream)"></div>
    <div class="critter" role="img" aria-label="Cartoon chick" style="--x:198px;--y:154px;--w:36px;--h:46px;--c:var(--sun)"></div>
    <div class="critter" role="img" aria-label="Cartoon owl" style="--x:504px;--y:151px;--w:36px;--h:44px;--c:var(--orange)"></div>
    <div class="critter" role="img" aria-label="Cartoon crab" style="--x:609px;--y:190px;--w:40px;--h:26px;--c:var(--salmon)"></div>
    <div class="critter" role="img" aria-label="Cartoon puppy" style="--x:176px;--y:280px;--w:38px;--h:44px;--c:var(--orange)"></div>
    <div class="critter" role="img" aria-label="Cartoon lion" style="--x:516px;--y:340px;--w:54px;--h:58px;--c:var(--orange)"></div>
    <div class="critter" role="img" aria-label="Rubber duck" style="--x:609px;--y:352px;--w:36px;--h:38px;--c:var(--sun)"></div>
    <div class="critter" role="img" aria-label="Cartoon pangolin" style="--x:100px;--y:352px;--w:56px;--h:40px;--c:var(--pink)"></div>
    <div class="critter" role="img" aria-label="Cartoon turtle" style="--x:210px;--y:364px;--w:60px;--h:30px;--c:var(--leaf)"></div>
    <div class="critter" role="img" aria-label="Cartoon giraffe" style="--x:345px;--y:397px;--w:50px;--h:86px;--c:var(--sun)"></div>
    <div class="critter" role="img" aria-label="Cartoon snake" style="--x:60px;--y:406px;--w:56px;--h:38px;--c:var(--leaf)"></div>
    <div class="critter" role="img" aria-label="Cartoon whale" style="--x:645px;--y:460px;--w:62px;--h:40px;--c:var(--grey)"></div>
    <div class="critter" role="img" aria-label="Cartoon frog" style="--x:540px;--y:466px;--w:40px;--h:36px;--c:var(--leaf)"></div>
    <div class="critter" role="img" aria-label="Cartoon elephant" style="--x:378px;--y:487px;--w:84px;--h:50px;--c:var(--sky)"></div>
    <div class="critter" role="img" aria-label="Cartoon gorilla" style="--x:213px;--y:481px;--w:42px;--h:46px;--c:var(--salmon)"></div>
    <div class="critter" role="img" aria-label="Cartoon owl" style="--x:291px;--y:520px;--w:30px;--h:38px;--c:var(--orange)"></div>
    <div class="critter" role="img" aria-label="Cartoon seahorse" style="--x:60px;--y:493px;--w:28px;--h:46px;--c:#7fa08e"></div>
    <div class="critter" role="img" aria-label="Cartoon frog" style="--x:123px;--y:553px;--w:40px;--h:36px;--c:var(--leaf)"></div>
    <div class="critter" role="img" aria-label="Cartoon crab" style="--x:27px;--y:577px;--w:42px;--h:26px;--c:var(--salmon)"></div>
    <div class="critter" role="img" aria-label="Cartoon giraffe" style="--x:516px;--y:583px;--w:44px;--h:76px;--c:var(--sun)"></div>
    <div class="critter" role="img" aria-label="Cartoon rhino" style="--x:108px;--y:625px;--w:72px;--h:44px;--c:var(--salmon)"></div>
    <div class="critter" role="img" aria-label="Cartoon zebra" style="--x:630px;--y:649px;--w:58px;--h:56px;--c:var(--grey)"></div>
    <div class="critter" role="img" aria-label="Cartoon cheetah" style="--x:231px;--y:694px;--w:82px;--h:56px;--c:var(--sun)"></div>
    <div class="critter" role="img" aria-label="Pastel rainbow" style="--x:344px;--y:715px;--w:58px;--h:44px;--c:var(--sun)"></div>
    <div class="critter" role="img" aria-label="Cartoon cat" style="--x:513px;--y:700px;--w:40px;--h:54px;--c:var(--cream)"></div>
    <div class="critter" role="img" aria-label="Rubber duck" style="--x:57px;--y:694px;--w:32px;--h:34px;--c:var(--sun)"></div>
    <div class="critter" role="img" aria-label="Cartoon puppy" style="--x:36px;--y:760px;--w:40px;--h:46px;--c:var(--orange)"></div>
    <div class="critter" role="img" aria-label="Cartoon clownfish" style="--x:141px;--y:757px;--w:52px;--h:32px;--c:var(--salmon)"></div>
    <div class="critter" role="img" aria-label="Cartoon crab" style="--x:294px;--y:772px;--w:36px;--h:24px;--c:var(--salmon)"></div>
    <div class="critter" role="img" aria-label="Cartoon crocodile" style="--x:408px;--y:772px;--w:86px;--h:30px;--c:var(--leaf)"></div>
    <div class="critter" role="img" aria-label="Cartoon snake" style="--x:609px;--y:760px;--w:66px;--h:40px;--c:var(--leaf)"></div>

    <section class="front-panel">
      <p class="claims">100% Natural | Vegan<span class="rule"></span>Palm Oil-Free</p>
      <h1 class="brand-name">Pippin &amp; Pals</h1>
      <h2 class="product-name">SHAMPOO BAR</h2>
      <p class="ingredients">Ingredients: Sodium hydroxide, prunus amygdalus dulcis oil, olea europaea oil, cocos nucifera oil, ricinus communis seed oil, simmondsia chinensia seed oil.</p>
      <address class="maker">Pippin &amp; Pals<br>Marlow Tessing House, London N7 4QB.<br>www.Pippin and pals.co.U.K.</address>
      <p class="weight">85 g</p>
      <p class="origin">Made in the U.K.</p>
    </section>
  </main>
</body>
</html>
```